Business Cards for a Junk Removal Company

Hello,
We are looking to have business cards designed that are simple, bold, easy to read, and right to the point. Please see the attachments for our logo files. We want the card to be yellow on both sides ( Color code Yellow: #FFE01B). The logo text font is (Rockstar Extra Bold) and this is also in the files attached. Please make the text black for the logo. On the back side of the card, you can use white and black for text. Thank you in advance for your hard work!

Front of card-
Harbor Haul Away (logo)
Back of card-
Harbor Haul Away
Donate - Recycle - Dispose
555-271-8093
www.harborhaulaway.example
info@harborhaulaway.example

Industry/Entity Type

Junk removal

Contact Information for Business Card

FRONT OF CARD- Harbor Haul Away (logo) BACK OF CARD- Harbor Haul Away Donate - Recycle - Dispose 555-271-8093 www.harborhaulaway.example info@harborhaulaway.example

Font styles to use
Other font styles liked:
• Rockstar Extra Bold

Colors
FFF300
FFF600
FEFA6F
FFFEC7
FFFEE8

Requirements
Must have
• Must have color code Yellow: #FFE01B for the background of front and back of the card

```html
<!DOCTYPE html>
<html lang="en">
<head>
<meta charset="utf-8">
<title>Harbor Haul Away – Business Cards</title>
<link href="https://fonts.googleapis.com/css2?family=Anton&display=swap" rel="stylesheet">
<style>
  :root {
    --backdrop: #979797;
    --card-yellow: #FFE01B;
    --ink: #0b0b0b;
  }
  html, body {
    margin: 0;
    padding: 0;
    width: 1200px;
    height: 1000px;
    overflow: hidden;
    background: var(--backdrop);
  }
  .sheet {
    display: block;
    width: 1200px;
    height: 1000px;
  }
  .card { fill: var(--card-yellow); }
  .ink { fill: var(--ink); }
  .wordmark, .tagline, .contact {
    font-family: "Anton", "Impact", sans-serif;
    fill: var(--ink);
    stroke: none;
    text-transform: uppercase;
    text-rendering: geometricPrecision;
  }
  .icon-stroke {
    fill: none;
    stroke: var(--ink);
  }
</style>
</head>
<body>
<svg class="sheet" viewBox="0 0 1200 1000" xmlns="http://www.w3.org/2000/svg">

  <!-- Front of card -->
  <g class="card-front">
    <rect class="card" x="183" y="192" width="351" height="615"/>
    <text class="wordmark wordmark-primary" transform="translate(372 788) rotate(-90)"
          x="0" y="0" font-size="135" textLength="578" lengthAdjust="spacingAndGlyphs">Harbor</text>
    <text class="wordmark wordmark-secondary" transform="translate(455 768) rotate(-90)"
          x="0" y="0" font-size="58" textLength="537" lengthAdjust="spacing">Haul Away</text>
  </g>

  <!-- Back of card -->
  <g class="card-back">
    <rect class="card" x="605" y="193" width="351" height="615"/>

    <g class="service-icons">
      <!-- donate: heart over hand -->
      <g class="icon-donate">
        <path class="ink" d="M671 284 L652 265 A11 11 0 0 1 671 250 A11 11 0 0 1 690 265 Z"/>
        <rect class="ink" x="633" y="290" width="12" height="28"/>
        <path class="ink" d="M648 292 L668 292 Q678 292 678 299 L692 293 Q706 289 710 297 L676 316 Q668 320 660 318 L648 314 Z"/>
      </g>
      <!-- recycle: three chasing arrows -->
      <g class="icon-recycle">
        <path class="icon-stroke" stroke-width="11" d="M760 272 L771 254 Q781 240 791 254 L797 264"/>
        <polygon class="ink" points="788,268 808,260 804,280"/>
        <path class="icon-stroke" stroke-width="11" d="M809 283 L818 300 Q824 313 808 314 L792 314"/>
        <polygon class="ink" points="794,303 778,314 794,326"/>
        <path class="icon-stroke" stroke-width="11" d="M772 314 L757 314 Q742 313 748 299 L753 290"/>
        <polygon class="ink" points="742,292 762,282 762,301"/>
      </g>
      <!-- dispose: trash can -->
      <g class="icon-trash">
        <rect class="ink" x="878" y="235" width="16" height="7" rx="2" transform="rotate(-8 886 238)"/>
        <rect class="ink" x="862" y="242" width="56" height="8" rx="2" transform="rotate(-8 890 246)"/>
        <path class="ink" d="M866 256 L914 256 L908 318 L872 318 Z"/>
        <g class="card">
          <rect x="875" y="263" width="4" height="48"/>
          <rect x="883" y="263" width="4" height="48"/>
          <rect x="891" y="263" width="4" height="48"/>
          <rect x="899" y="263" width="4" height="48"/>
        </g>
      </g>
    </g>

    <g class="tagline">
      <text x="627" y="440" font-size="80" textLength="306" lengthAdjust="spacingAndGlyphs">Donate</text>
      <text x="627" y="515" font-size="74" textLength="306" lengthAdjust="spacingAndGlyphs">Recycle</text>
      <text x="627" y="588" font-size="72" textLength="306" lengthAdjust="spacingAndGlyphs">Dispose</text>
    </g>

    <g class="contact">
      <text class="contact-phone" x="627" y="660" font-size="42" textLength="306" lengthAdjust="spacingAndGlyphs">555-271-8093</text>
      <text class="contact-web" x="627" y="687" font-size="25" textLength="306" lengthAdjust="spacingAndGlyphs">www.harborhaulaway.example</text>
      <text class="contact-email" x="627" y="710" font-size="20" textLength="306" lengthAdjust="spacingAndGlyphs">info@harborhaulaway.example</text>
    </g>

    <g class="wordmark wordmark-small">
      <text x="725" y="765" font-size="27" textLength="111" lengthAdjust="spacingAndGlyphs">Harbor</text>
      <text x="730" y="781" font-size="12" textLength="102" lengthAdjust="spacing">Haul Away</text>
    </g>
  </g>
</svg>
</body>
</html>
```